Flyer-Design für Amerikanische Chiropraktik
Zielgruppe
Praxis für Amerikanische Chiropraktik
Zielgruppe: Gesundheitsbewusste Menschen, gerne gebildet, Affinität zu Sport/Yoga etc.
Flyer soll modern und hochwertig sein (Zielgruppe auch Privatversicherte und Büroleute)
Aufgabenstellung
Bitte keine Schnörkel.
Klare Linien. Straight einfach
Positive Vibes
Website ist nicht final fertig. Das blau/grau und das Grün wird aber aller Voraussicht nach Weiter verwendet. Falls das rot verwendet wird eher nicht so oft bitte.
Sehr gerne für die Überschriften die gleichen Balken unter den Überschriften für den Flyer verwenden.
Flyer bei Nordra Druck ist 99x210 mm (ich denke mit etwas Spiel am Rand für den Druck.) 6 Seiten.
Auf der letzten Seite (sollte die mittlere Rückseite sein) bitte Kontaktdaten und evtl Portraitbild.

```html
<!DOCTYPE html>
<html lang="de">
<head>
<meta charset="utf-8">
<title>Chiropraktik Kasimir Holt – Flyer Innenseite</title>
<link href="https://fonts.googleapis.com/css2?family=Josefin+Sans:wght@300;400&display=swap" rel="stylesheet">
<style>
  :root {
    --panel-dark: #3e3e40;
    --paper: #e2e2e2;
    --accent-blue: #2f87b6;
    --soft-blue: #a8c8df;
    --gold: #b7a180;
    --ink: #3a3a3a;
    --line: #8c8c8c;
    --photo-light: #efe9e2;
    --photo-mid: #d9cdbf;
    --photo-dark: #b8a58c;
    --icon-fill: #d6d6d6;
  }
  * { margin: 0; padding: 0; box-sizing: border-box; }
  html, body { width: 1200px; height: 600px; overflow: hidden; background: var(--paper); }
  .spread {
    position: relative; width: 1200px; height: 600px; background: var(--paper);
    font-family: "Josefin Sans", sans-serif; color: var(--ink); overflow: hidden;
  }
  .cover {
    position: absolute; left: 0; top: 0; width: 300px; height: 600px;
    background: var(--panel-dark); text-align: center;
  }
  .cover-line {
    position: absolute; left: 0; width: 300px; font-size: 15.5px; line-height: 18px;
    font-weight: 300; white-space: nowrap;
  }
  .cover-kicker, .cover-footer { color: var(--soft-blue); }
  .cover-claim { color: #f2f2f2; }
  .brand-dot {
    position: absolute; left: 107px; top: 100px; width: 86px; height: 86px;
    border-radius: 50%; border: 2px solid var(--gold);
  }
  .brand-name {
    position: absolute; left: 0; top: 220px; width: 300px; font-size: 24px; line-height: 26px;
    font-weight: 300; color: var(--gold); letter-spacing: 2px; white-space: nowrap;
  }
  .divider { position: absolute; width: 1px; background: var(--line); }
  .block { position: absolute; width: 234px; }
  .heading {
    position: absolute; width: 234px; font-size: 14px; line-height: 20px; font-weight: 400;
    color: var(--accent-blue); white-space: nowrap;
  }
  .heading .ln { display: block; }
  .heading-right { text-align: right; }
  .text { font-size: 10.2px; line-height: 14.1px; font-weight: 300; color: var(--ink); }
  .ln {
    display: block; white-space: nowrap; text-align: justify; text-align-last: justify;
  }
  .ln.end { text-align-last: left; }
  .photo {
    position: absolute; width: 234px; height: 156px;
    background: linear-gradient(135deg, var(--photo-light) 0%, var(--photo-mid) 55%, var(--photo-dark) 100%);
  }
  .icon-badge {
    position: absolute; border-radius: 50%; border: 1.2px solid #2a2a2a; background: var(--icon-fill);
  }
</style>
</head>
<body>
<div class="spread">
  <section class="cover">
    <p class="cover-line cover-kicker" style="top:32px;">IHR WEG ZU MEHR WOHLBEFINDEN</p>
    <div class="brand-dot"></div>
    <p class="brand-name">KASIMIR HOLT</p>
    <p class="cover-line cover-claim" style="top:320px;">MODERN.<br>URSÄCHLICH.<br>ANDERS.</p>
    <p class="cover-line cover-footer" style="top:558px;">TIME TO CONNECT YOUR BRAIN.</p>
  </section>

  <div class="divider" style="left:600px; top:47px; height:536px;"></div>
  <div class="divider" style="left:905px; top:29px; height:536px;"></div>

  <!-- Spalte 1 -->
  <h2 class="heading" style="left:332px; top:30px;">
    <span class="ln" style="text-align:justify; text-align-last:justify;">WAS IST AMERIKANISCHE CHIRO-</span>
    <span class="ln">PRAKTIK?</span>
  </h2>
  <div class="icon-badge" role="img" aria-label="Symbol eines Gehirns" style="left:318px; top:84px; width:105px; height:105px;"></div>
  <p class="block text" style="left:433px; top:72px; width:133px;">
    <span class="ln">Amerikanische Chiropraktik</span>
    <span class="ln">ist eine eigenständige, ganz-</span>
    <span class="ln">heitliche und vitalistische</span>
    <span class="ln">Form der Gesundheitspfle-</span>
    <span class="ln">ge, die darauf ausgerichtet</span>
    <span class="ln">ist, Gesundheit und Funktion</span>
    <span class="ln">des menschlichen Körpers</span>
    <span class="ln">wiederherzustellen und zu</span>
    <span class="ln end">erhalten.</span>
  </p>
  <p class="block text" style="left:332px; top:213px;">
    <span class="ln">Sie ist sowohl eine evidenzbasierte Wissenschaft</span>
    <span class="ln">als auch eine Heilkunst und eine Philosophie, die</span>
    <span class="ln">nach der optimalen Funktion des Nervensystems</span>
    <span class="ln end">strebt.</span>
  </p>
  <div class="photo" role="img" aria-label="Foto: Chiropraktorin behandelt eine liegende Patientin an der Hüfte" style="left:332px; top:278px;"></div>
  <h2 class="heading" style="left:332px; top:450px;"><span class="ln" style="text-align:justify; text-align-last:justify;">WIE FUNKTIONIERT CHIROPRAKTIK?</span></h2>
  <p class="block text" style="left:332px; top:477px;">
    <span class="ln">Der Körper wird von seinem Nervensystem gesteu-</span>
    <span class="ln">ert. Es ist dafür verantwortlich, wie ein Mensch sei-</span>
    <span class="ln">ne Umwelt wahrnimmt und durch das Leben geht.</span>
    <span class="ln">Über das Nervensystem empfängt und sendet</span>
    <span class="ln">das Gehirn fortwährend Informationen an Organe,</span>
    <span class="ln">Muskeln und alle anderen Strukturen. Seine opti-</span>
    <span class="ln end">male Funktion ist demnach von größter Bedeutung.</span>
  </p>

  <!-- Spalte 2 -->
  <div class="photo" role="img" aria-label="Foto: Hände eines Chiropraktors auf dem Rücken einer liegenden Patientin" style="left:636px; top:34px;"></div>
  <p class="block text" style="left:636px; top:205px;">
    <span class="ln">Im besten Fall werden Körper und Psyche über das</span>
    <span class="ln">Nervensystem in Balance gehalten. Dazu muss</span>
    <span class="ln">alles störungsfrei miteinander vernetzt sein. Fehl-</span>
    <span class="ln">stellungen und Blockaden können die Vernetzung</span>
    <span class="ln">stören: Es kommt zu sogenannten Subluxationen.</span>
    <span class="ln">Das physische und psychische Gleichgewicht gerät</span>
    <span class="ln end">ins Wanken.</span>
  </p>
  <div class="photo" role="img" aria-label="Foto: Chiropraktische Justierung an der Wirbelsäule einer Patientin" style="left:636px; top:320px;"></div>
  <p class="block text" style="left:636px; top:490px;">
    <span class="ln">Die Folgen können sehr vielfältig sein. Muskelver-</span>
    <span class="ln">spannungen, Nackenschmerzen, Kopfschmerzen</span>
    <span class="ln">oder Rückenschmerzen können die Folge sein.</span>
    <span class="ln">Oft bleiben solche Subluxationen über Jahre un-</span>
    <span class="ln">bemerkt, bevor sie Schmerzen und/oder psycho-</span>
    <span class="ln end">emotionale Symptome verursachen.</span>
  </p>

  <!-- Spalte 3 -->
  <h2 class="heading heading-right" style="left:934px; top:30px;">
    <span class="ln">WAS IST EIGENTLICH EINE</span>
    <span class="ln">SUBLUXATION?</span>
  </h2>
  <div class="icon-badge" role="img" aria-label="Symbol einer Wirbelsäule" style="left:917px; top:64px; width:60px; height:60px;"></div>
  <p class="block text" style="left:934px; top:75px;">
    <span class="ln" style="margin-left:52px;">Wir definieren eine vertebrale Subluxa-</span>
    <span class="ln" style="margin-left:52px;">tion als ein dysfunktionales Gebiet in</span>
    <span class="ln" style="margin-left:52px;">der Wirbelsäule, dass sich aufgrund sei-</span>
    <span class="ln" style="margin-left:52px;">nes Einflusses auf das Nervensystem</span>
    <span class="ln">negativ auf die Gesundheit und das Wohlbefinden</span>
    <span class="ln">auswirkt. Die Funktion der Wirbelsäule als wichtiger</span>
    <span class="ln end">Informationsgeber für das Gehirn ist gestört.</span>
  </p>
  <h2 class="heading" style="left:934px; top:186px;"><span class="ln" style="text-align:justify; text-align-last:justify;">WIE ENTSTEHEN SUBLUXATIONEN?</span></h2>
  <p class="block text" style="left:934px; top:212px;">
    <span class="ln">Chronischer Stress, Überbelastung, wenig Bewe-</span>
    <span class="ln">gung, Traumata sind Beispiele die das Nervensys-</span>
    <span class="ln">tem in seiner Funktion beeinträchtigen können</span>
    <span class="ln">(Perrault et al., 2015). Da zwischen Nervensystem</span>
    <span class="ln">und Bewegungsapparat eine starke Beziehung be-</span>
    <span class="ln">steht, können sich diese Faktoren auch auf die Ge-</span>
    <span class="ln end">lenke auswirken (Tanabashi, 2017).</span>
  </p>
  <h2 class="heading" style="left:934px; top:323px;"><span class="ln" style="text-align:justify; text-align-last:justify;">WIE HELFEN WIR? DIE JUSTIERUNG</span></h2>
  <div class="icon-badge" role="img" aria-label="Symbol zweier Hände bei der Justierung" style="left:918px; top:352px; width:62px; height:62px;"></div>
  <p class="block text" style="left:934px; top:350px;">
    <span class="ln" style="margin-left:54px;">Die chiropraktische Justierung korrigiert</span>
    <span class="ln" style="margin-left:54px;">eine Subluxation, indem sie das schad-</span>
    <span class="ln" style="margin-left:54px;">hafte neurologische Muster durch-</span>
    <span class="ln" style="margin-left:54px;">bricht. Durch einen sanften und ge-</span>
    <span class="ln" style="margin-left:54px;">zielten Impuls wird die physiologische</span>
    <span class="ln">Beweglichkeit und Position eines Gelenkes wieder</span>
    <span class="ln">hergestellt und faszialer Adhäsionen gelöst. Die Im-</span>
    <span class="ln">pulse führen zu einer messbaren Verbesserung in</span>
    <span class="ln">der Funktion hinsichtlich der Beziehung zwischen</span>
    <span class="ln">Nervensystem und Bewegungsapparat (Hauvold</span>
    <span class="ln">et al., 2021). Der chiropraktische Impuls wirkt auf</span>
    <span class="ln">struktureller Ebene (am Gelenk) und im Nervensys-</span>
    <span class="ln">tem. Der Informationsfluss zwischen Körper und</span>
    <span class="ln">Nervensystem wird harmonisiert und Selbsthei-</span>
    <span class="ln">lungskräfte aktiviert, um dir eine volle Funktionalität</span>
    <span class="ln end">und mehr Lebensqualität zu ermöglichen.</span>
  </p>
</div>
</body>
</html>
```